Water Filter Company Needs Bizz Cards!!

Need business cards for my company. We sell whole home water filters and salt free water softeners. No more buying bottled water. Our filtering units filter out all heavy metals, chlorine, and VOC's, last 15 years, and are maintenance free and supply your whole home with spring quality alkaline water. Our Salt free water conditioners, eliminate hard water and scale, without lowering the ph, or TDS's (total Dissolved solids)

I think this is the color code we are using on my site. My logo looks good behind it. #192841

Website will be www.Brovexa.com

Industry/Entity Type

Water Purification

Contact Information for Business Card

For now, just insert standard Dummy text. I need these text lines for the info to be editable so i can make them for multiple employees. I do have Photoshop and illustrator, unless there is a simpler program i can use solely for biz cards

Font styles to use
Sans Serif

Requirements
Must have
• Use my preexisting logo.

www.BroVexa.com

Spring Quality Alkaline Water at every tap.

List out services. Whole Home Water Filters, Salt Free Water Softeners, Clarimont KT7, UV Sterilizers
Nice to have
• I think this is the color code we are using on my site. My logo looks good behind it. #192841 or black. Please no white or light blue backgrounds.

Maybe a picture of my tank.

Slogan like Spring Quality Alkaline Water at every tap.
And just list the services Whole Home Water Filters, Salt Free Water Softeners, Clarimont KT7, UV Sterilizers

I think I would like to not have a contrasting textured logo like I see on some of them. I may use it for my personal cards, but new employees may not want the extra expense.
Should not have
• A different logo than the one provided.

White or baby blue backgrounds. Use the color code, or blacks.

```html
<!DOCTYPE html>
<html lang="en">
<head>
<meta charset="utf-8">
<title>Brovexa Business Card</title>
<link rel="stylesheet" href="https://fonts.googleapis.com/css2?family=Montserrat:wght@400;500;600;700&family=Open+Sans:wght@400;600&display=swap">
<style>
  :root {
    --stage: #dcdcda;
    --night: #0e1424;
    --navy: #192841;
    --navy-deep: #111c33;
    --sky: #1aa3e0;
    --band: #0d8fd6;
    --ink-light: #e6e9ee;
    --ink-soft: #c3cad6;
    --rule: #4a5670;
    --steel: #c8cacd;
    --white: #ffffff;
  }
  * { box-sizing: border-box; margin: 0; padding: 0; }
  html, body { width: 1200px; height: 801px; overflow: hidden; }
  body {
    background: var(--stage);
    font-family: "Montserrat", sans-serif;
    position: relative;
  }
  .card {
    position: absolute;
    top: 245px;
    width: 540px;
    height: 310px;
    overflow: hidden;
    box-shadow: 0 6px 18px rgba(0,0,0,.18);
  }

  /* Front */
  .card-front {
    left: 40px;
    background: linear-gradient(160deg, #141d31 0%, var(--night) 100%);
  }
  .front-brand {
    position: absolute; left: 34px; top: 104px;
    display: flex; align-items: center; gap: 10px;
  }
  .brand-dot { width: 18px; height: 18px; border-radius: 50%; background: var(--sky); }
  .brand-name { font-weight: 700; font-size: 34px; color: var(--sky); letter-spacing: -0.5px; }
  .front-divider {
    position: absolute; left: 262px; top: 40px;
    width: 1px; height: 160px; background: var(--rule);
  }
  .contact { position: absolute; left: 282px; top: 42px; color: var(--ink-soft); }
  .contact-name { font-weight: 700; font-size: 18px; color: var(--sky); letter-spacing: .5px; }
  .contact-role { font-weight: 700; font-size: 13px; margin: 2px 0 10px; color: var(--ink-light); }
  .contact-line { font-size: 12px; line-height: 18px; display: flex; align-items: center; gap: 7px; }
  .contact-line svg { width: 12px; height: 12px; flex: none; }
  .address { margin-bottom: 4px; }
  .slogan-band {
    position: absolute; left: 0; bottom: 30px;
    width: 100%; height: 40px;
    background: var(--band);
    display: flex; align-items: center;
  }
  .slogan {
    color: var(--white); font-size: 15px; font-weight: 500;
    padding-left: 30px;
  }
  .band-end {
    position: absolute; right: 0; bottom: 70px;
    width: 58px; height: 24px; background: var(--steel);
  }

  /* Back */
  .card-back {
    left: 620px;
    background: linear-gradient(160deg, var(--navy) 0%, var(--navy-deep) 100%);
  }
  .back-brand {
    position: absolute; left: 40px; top: 78px;
    display: flex; align-items: center; gap: 12px;
  }
  .back-brand .brand-dot { width: 22px; height: 22px; }
  .back-brand .brand-name { font-size: 48px; }
  .product-shot {
    position: absolute; left: 300px; top: 26px;
    width: 214px; height: 214px;
    border-radius: 6px;
    background: linear-gradient(90deg, #d9dcc3 0%, #b9bcc2 45%, #24272c 100%);
    opacity: .85;
  }
  .services {
    position: absolute; left: 40px; top: 196px;
    list-style: none;
    font-family: "Open Sans", sans-serif;
    color: var(--white); font-size: 15px; line-height: 21px;
  }
  .services li { display: flex; align-items: center; gap: 7px; }
  .services li::before {
    content: ""; width: 7px; height: 7px; border-radius: 50%; background: var(--sky);
  }
</style>
</head>
<body>

<section class="card card-front" aria-label="Business card front">
  <div class="front-brand">
    <span class="brand-dot"></span>
    <span class="brand-name">Brovexa</span>
  </div>
  <div class="front-divider"></div>
  <div class="contact">
    <p class="contact-name">MARLOW KESTRANE</p>
    <p class="contact-role">Director</p>
    <p class="contact-line">48 Linden Quay,</p>
    <p class="contact-line address">Harbour District</p>
    <p class="contact-line">
      <svg viewBox="0 0 12 12"><path d="M2 1h3l1 3-2 1a7 7 0 0 0 3 3l1-2 3 1v3a1 1 0 0 1-1 1A10 10 0 0 1 1 2a1 1 0 0 1 1-1z" fill="#1aa3e0"/></svg>
      84 0900 555 214
    </p>
    <p class="contact-line">
      <svg viewBox="0 0 12 12"><rect x="1" y="2.5" width="10" height="7" fill="#1aa3e0"/><path d="M1 2.5l5 4 5-4" stroke="#0e1424" fill="none"/></svg>
      marlow@brovexa.com
    </p>
    <p class="contact-line">
      <svg viewBox="0 0 12 12"><circle cx="6" cy="6" r="5" fill="#1aa3e0"/><path d="M1 6h10M6 1c-2 3-2 7 0 10M6 1c2 3 2 7 0 10" stroke="#0e1424" stroke-width=".8" fill="none"/></svg>
      www.brovexa.com
    </p>
  </div>
  <div class="band-end"></div>
  <div class="slogan-band">
    <p class="slogan">Spring Quality Alkaline Water at every tap.</p>
  </div>
</section>

<section class="card card-back" aria-label="Business card back">
  <div class="back-brand">
    <span class="brand-dot"></span>
    <span class="brand-name">Brovexa</span>
  </div>
  <div class="product-shot" role="img" aria-label="Photo of a filter tank, a UV sterilizer and a softener unit"></div>
  <ul class="services">
    <li>Whole home water filters</li>
    <li>Salt free water softeners</li>
    <li>Clarimont KT7</li>
    <li>UV Sterilizers</li>
  </ul>
</section>

</body>
</html>
```